" Clínica médica que atua nas diversas especialidades e realiza atendimentos particulares a preços acessíveis, podendo futuramente atender planos de saúde. "

```html
<!DOCTYPE html>
<html lang="pt-BR">
<head>
<meta charset="utf-8">
<title>VitaClin — Resultados rápidos</title>
<link rel="stylesheet" href="https://fonts.googleapis.com/css2?family=Open+Sans:wght@400;600;700;800&display=swap">
<style>
  :root{
    --bg:#f1f2f1;
    --white:#ffffff;
    --green-dark:#2f6b34;
    --green:#4a9a3c;
    --green-list:#5aa844;
    --green-line:rgba(255,255,255,.25);
    --text-dark:#2b4a2e;
    --grey-light:#eceeed;
    --grey-mid:#d7dbd9;
  }
  *{box-sizing:border-box;margin:0;padding:0}
  html,body{width:1200px;height:1200px;overflow:hidden}
  body{background:var(--bg);font-family:"Open Sans",Arial,sans-serif;display:flex;align-items:center;justify-content:center}
  .page{width:640px;height:1130px;background:var(--white);display:flex;flex-direction:column;box-shadow:0 6px 30px rgba(0,0,0,.08)}
  .hero{position:relative;height:510px;border-top:6px solid var(--green-dark);overflow:hidden}
  .hero-photo{position:absolute;right:0;top:0;width:400px;height:100%;
    background:radial-gradient(ellipse at 60% 55%,#e9d6c8 0%,#f3ece6 45%,#ffffff 75%)}
  .hero-copy{position:absolute;left:36px;top:34px;z-index:2}
  .hero-title{color:var(--green-dark);font-weight:800;font-size:46px;line-height:1.12;letter-spacing:-.5px}
  .tag{display:inline-block;vertical-align:middle;background:var(--green-dark);color:var(--white);font-size:13px;font-weight:600;padding:3px 22px;margin-left:8px}
  .brand{display:flex;align-items:center;gap:8px;margin-top:28px;color:var(--green);font-weight:700;font-size:24px}
  .brand-dot{width:16px;height:16px;border-radius:50%;background:var(--green)}
  .cards{display:flex;height:300px}
  .card{flex:1;padding:28px 32px}
  .card-guide{background:linear-gradient(135deg,#ffffff 0%,var(--grey-light) 100%)}
  .card-collect{background:linear-gradient(135deg,var(--grey-mid) 0%,#f4f5f4 70%)}
  .card-title{color:var(--green-dark);font-weight:800;font-size:36px;line-height:1.12}
  .card-text{color:var(--green-dark);font-weight:600;font-size:22px;line-height:1.3;margin-top:18px}
  .services{flex:1;background:var(--green-list);display:flex;flex-direction:column}
  .services-title{background:var(--green);color:var(--white);font-weight:700;font-size:30px;padding:22px 36px;border-bottom:2px solid var(--green-dark)}
  .services-list{display:grid;grid-template-columns:1fr 1fr;column-gap:28px;padding:10px 36px}
  .services-list ul{list-style:none}
  .services-list li{color:var(--white);font-size:16px;padding:12px 0;border-bottom:1px solid var(--green-line)}
</style>
</head>
<body>
  <main class="page">
    <section class="hero">
      <div class="hero-photo" role="img" aria-label="Foto de uma família sorridente: pai, mãe e três crianças abraçados"></div>
      <div class="hero-copy">
        <h1 class="hero-title">Resultados<br>rápidos.<br>Marcação de<br>Exames<span class="tag">MAIS</span></h1>
        <div class="brand"><span class="brand-dot"></span>VitaClin</div>
      </div>
    </section>
    <section class="cards">
      <div class="card card-guide">
        <h2 class="card-title">Orientações<br>de Exames</h2>
        <p class="card-text">Saiba mais</p>
      </div>
      <div class="card card-collect" role="img" aria-label="Foto de um carro de coleta externa ao fundo">
        <h2 class="card-title">Coleta<br>Externa</h2>
        <p class="card-text">Faça o<br>agendamento<br>de sua Coleta</p>
      </div>
    </section>
    <section class="services">
      <h2 class="services-title">Exames e consultas</h2>
      <div class="services-list">
        <ul>
          <li>PET-CT</li>
          <li>Tomografia 64 canais</li>
          <li>Ressonância Magnética 1.5 tesla</li>
          <li>Tomossíntese</li>
          <li>Medicina Nuclear</li>
        </ul>
        <ul>
          <li>Cardiologia</li>
          <li>Clínica Médica (clínico geral)</li>
          <li>Dermatologia</li>
          <li>Endocrinologia</li>
          <li>Gastro-hepatologia</li>
        </ul>
      </div>
    </section>
  </main>
</body>
</html>
```